Bright Harbor Realty

We need a good looking flyer for our real estate company to impress people who are considering to sell their homes for as low as 1.5% listing commission. Please see flyer examples for reference.
555-318-4906

```html
<!DOCTYPE html>
<html lang="en">
<head>
<meta charset="utf-8">
<title>Bright Harbor Realty – Just Sold Postcard</title>
<link rel="stylesheet" href="https://fonts.googleapis.com/css2?family=Roboto+Condensed:ital,wght@0,400;0,700;1,400;1,700;1,900&family=Lato:wght@400;700&display=swap">
<style>
  :root {
    --stage: #2e2e2e;
    --paper: #ffffff;
    --wash: #f1f2f4;
    --blue: #0f4aa8;
    --red: #e0161b;
    --ink: #1a1a1a;
    --rule: #222222;
  }
  * { box-sizing: border-box; margin: 0; padding: 0; }
  html, body { width: 1200px; height: 1200px; overflow: hidden; }
  body { background: var(--stage); position: relative; font-family: "Roboto Condensed", sans-serif; color: var(--ink); }

  .card { position: absolute; top: 200px; width: 570px; height: 800px; background: var(--paper); overflow: hidden; }
  .card--front { left: 16px; background: linear-gradient(180deg, #ffffff 0%, var(--wash) 55%, #ffffff 100%); }
  .card--back { left: 614px; }

  /* brand */
  .brand { position: absolute; display: flex; align-items: center; gap: 8px; }
  .brand__mark { width: 14px; height: 14px; background: var(--blue); flex: none; }
  .brand__name { font-weight: 700; color: var(--blue); line-height: 1.05; }
  .card--front .brand { left: 22px; top: 48px; width: 120px; }
  .card--front .brand__name { font-size: 20px; }
  .card--back .brand { left: 190px; top: 296px; }
  .card--back .brand__name { font-size: 30px; }

  /* front header */
  .pitch { position: absolute; right: 26px; top: 22px; text-align: right; font-style: italic; }
  .pitch__line1 { font-size: 18px; }
  .pitch__line1 b, .offer b { color: var(--blue); font-weight: 700; }
  .pitch__line2 { font-size: 18px; font-weight: 700; }
  .pitch__call { font-size: 12px; margin-top: 3px; }
  .phone { color: var(--blue); font-weight: 900; font-style: italic; }
  .pitch .phone { font-size: 27px; line-height: 1; }

  .headline { position: absolute; left: 116px; top: 120px; width: 338px; display: flex; align-items: center; gap: 8px; }
  .headline::before, .headline::after { content: ""; flex: 1; height: 2px; background: var(--rule); }
  .headline h1 { font-size: 46px; font-weight: 900; font-style: italic; color: var(--red); letter-spacing: -0.5px; line-height: 1; }

  /* listings */
  .listing { position: absolute; width: 236px; text-align: center; }
  .listing__photo { width: 236px; height: 165px; border: 3px solid var(--blue); border-radius: 10px; }
  .listing__addr { font-size: 11px; font-weight: 700; font-style: italic; line-height: 13.5px; margin-top: 6px; }
  .listing__price { color: var(--red); }
  .photo-a { background: linear-gradient(180deg, #a9cbe8 0%, #d9d7a2 45%, #6aa84a 75%, #bdbdbd 100%); }
  .photo-b { background: linear-gradient(180deg, #8fb8e4 0%, #c9d6e6 35%, #8b8f8f 55%, #5f9a3c 80%); }
  .photo-c { background: linear-gradient(180deg, #2f7fd6 0%, #9fd0ef 35%, #cfe6f2 55%, #5ea83c 78%, #c9bfae 100%); }
  .photo-d { background: linear-gradient(180deg, #b9d3ee 0%, #c8a98f 40%, #a88a74 65%, #9a9a9a 100%); }

  /* did you know */
  .facts { position: absolute; left: 24px; top: 584px; width: 246px; }
  .facts h2 { font-size: 20px; font-weight: 700; color: var(--red); line-height: 1.05; }
  .facts p { font-size: 10.5px; line-height: 13.5px; text-align: justify; }
  .facts .call { font-size: 10px; font-weight: 700; margin-top: 6px; }
  .facts .phone { font-size: 21px; font-style: normal; font-weight: 700; line-height: 1.05; }

  .agent { position: absolute; left: 34px; top: 697px; width: 122px; height: 122px; border-radius: 50%; border: 3px solid var(--blue); background: radial-gradient(circle at 50% 35%, #c9ccd1 0%, #8e949b 55%, #3a3f45 100%); }

  /* back */
  .features-title { position: absolute; left: 24px; top: 22px; font-size: 33px; font-weight: 700; color: var(--blue); line-height: 1; padding-bottom: 3px; border-bottom: 2px solid var(--blue); letter-spacing: -0.3px; }
  .features { position: absolute; top: 74px; list-style: none; font-family: "Lato", sans-serif; font-size: 11.5px; color: #2a2a2a; }
  .features li { height: 33.6px; position: relative; padding-left: 15px; }
  .features li::before { content: ""; position: absolute; left: 0; top: 6px; width: 4px; height: 4px; border-radius: 50%; background: var(--blue); }
  .features--left { left: 24px; }
  .features--right { left: 316px; }

  .offer { position: absolute; left: 24px; top: 440px; font-size: 17px; font-style: italic; line-height: 22px; }
  .offer strong { font-weight: 700; }
  .contact { position: absolute; right: 22px; top: 432px; text-align: right; font-style: italic; }
  .contact__call { font-size: 12px; }
  .contact .phone { font-size: 25px; line-height: 1; }

  .stamp { position: absolute; left: 497px; top: 566px; width: 49px; height: 49px; border: 1px solid var(--rule); }
  .address-lines { position: absolute; left: 415px; top: 654px; width: 131px; }
  .address-lines span { display: block; height: 1px; background: var(--rule); margin-bottom: 20px; opacity: .7; }
</style>
</head>
<body>

<section class="card card--front">
  <div class="brand"><span class="brand__mark"></span><span class="brand__name">Bright Harbor Realty</span></div>

  <div class="pitch">
    <div class="pitch__line1">List for <b>1.5% Commission,</b></div>
    <div class="pitch__line2">Still Receive Top Marketing!</div>
    <div class="pitch__call">Call Us Today and Save Thousands!</div>
    <div class="phone">555-318-4906</div>
  </div>

  <div class="headline"><h1>JUST SOLD</h1></div>

  <article class="listing" style="left:33px;top:172px">
    <div class="listing__photo photo-a" role="img" aria-label="Photo of a sold single-storey yellow home with garage"></div>
    <p class="listing__addr">1 1713 Larkspur Circle<br>Wellington, FL 33414 - <span class="listing__price">$250,000</span></p>
  </article>
  <article class="listing" style="left:300px;top:172px">
    <div class="listing__photo photo-b" role="img" aria-label="Photo of a sold grey stone ranch home with lawn"></div>
    <p class="listing__addr">1631 1 E Meadowlark Drive<br>Loxahatchee, FL 33470 - <span class="listing__price">$280,000</span></p>
  </article>
  <article class="listing" style="left:33px;top:374px">
    <div class="listing__photo photo-c" role="img" aria-label="Photo of a sold light blue home with palm trees"></div>
    <p class="listing__addr">13972 Willowbend Circle<br>Wellington, FL 33414 - <span class="listing__price">$335,000</span></p>
  </article>
  <article class="listing" style="left:300px;top:374px">
    <div class="listing__photo photo-d" role="img" aria-label="Photo of sold two-storey townhomes with parked cars"></div>
    <p class="listing__addr">2062 Seabreeze Circle E<br>Deerfield Beach, FL 33442 - <span class="listing__price">$229,500</span></p>
  </article>
  <article class="listing" style="left:305px;top:575px">
    <div class="listing__photo photo-d" role="img" aria-label="Photo of sold two-storey townhomes on a quiet street"></div>
    <p class="listing__addr">513 5 Fairway Oaks Drive<br>Atlantis, FL 33462 - <span class="listing__price">$550,000</span></p>
  </article>

  <div class="facts">
    <h2>Did You Know?</h2>
    <p>On average, our customers<br>save <b>$8,750</b> when they choose us... and they still receive top marketing, service and representation!</p>
    <p class="call">Call Us Today and Save Thousands!</p>
    <div class="phone">555-318-4906</div>
  </div>

  <div class="agent" role="img" aria-label="Headshot of the listing agent"></div>
</section>

<section class="card card--back">
  <h2 class="features-title">FEATURES:</h2>
  <ul class="features features--left">
    <li>High Definition HDR Photography</li>
    <li>Aerial Photography</li>
    <li>Live Video Walk-Through of Home</li>
    <li>RoomScope 3D Floorplan</li>
  </ul>
  <ul class="features features--right">
    <li>For Sales Stake Sign</li>
    <li>Socialine Advertising</li>
    <li>Promoted on All Real Estate Websites</li>
    <li>Listing on MLS (Multiple Listing Services)</li>
  </ul>

  <div class="brand"><span class="brand__mark"></span><span class="brand__name">Bright Harbor Realty</span></div>

  <div class="offer">List for <b>1.5% Commission,</b><br><strong>Still Receive Top Marketing!</strong></div>
  <div class="contact">
    <div class="contact__call">Call Us Today and Save Thousands!</div>
    <div class="phone">555-318-4906</div>
  </div>

  <div class="stamp"></div>
  <div class="address-lines"><span></span><span></span><span></span></div>
</section>

</body>
</html>
```